Inspirational Quote Poster for Employees

For this project, we need a simple yet high-impact poster template that will be customized for each of our employees with a personalized inspirational quote and color scheme. This template should allow us to quickly and easily customize the text and colors in the poster without a lot of effort.

The poster design should consist of:
- A stylized text area to contain the main text of the quote
- A separate text area to contain the source of quote
- A background that complements the color and style of the text

Text may use different typographic effects (such as color, stroke weight, italicization, font size changes, drop shadows) to draw attention to words in the quote; the source of the quote may be formatted the same as the main text of the quote, or may be formatted differently to distinguish it from the main quote.

The background may be simply a single color, subtle texture, gradients, halftone effects, or other color/texture effects may be used to complement the text.

Examples of the types of posters envisioned by this project:
- http://www.pinvelora.example/marcusdtelford/quillbase-job-1/

Sample quotes to use to build your poster - choose whichever one you want, but be certain that the poster design will handle both long and short quotes:
- "Happiness in intelligent people is the rarest thing I know" - Walden Prosket
- "Wanting to be someone else is a waste of the person you are." - Rolf Dintey
- "Experience is not what happens to you. It is what you do with what happens to you." - Ferris Mundell
- "Simplicity is the ultimate in sophistication." - Rinaldo de Pavesco
- "You will get all you want in life if you help enough other people get what they want." - Tad Pomfrey
- "Hell, there are no rules here — we're trying to accomplish something." - Gareth Vullane

Industry/Entity Type

Quote

Requirements
Must have
• Final deliverable must be:
• - Formatted for an 18” x 24” poster (in portrait orientation)
• - Delivered in Adobe InDesign, Adobe Illustrator, or Extended PostScript format
• - Use CMYK color mode
• - Be print-ready at 300dpi resolution
• - Include any fonts used in the template

```html
<!DOCTYPE html>
<html lang="en">
<head>
<meta charset="utf-8">
<title>Simplicity — Quote Poster</title>
<link rel="stylesheet" href="https://fonts.googleapis.com/css2?family=Poiret+One&family=Questrial&display=swap">
<style>
  :root {
    --poster-bg: #000000;
    --quote-yellow: #f2ee1e;
    --source-white: #ffffff;
  }
  * { margin: 0; padding: 0; box-sizing: border-box; }
  html, body {
    width: 848px;
    height: 1200px;
    overflow: hidden;
    background: var(--poster-bg);
  }
  .poster {
    position: relative;
    width: 848px;
    height: 1200px;
    background: var(--poster-bg);
    overflow: hidden;
  }
  .quote {
    color: var(--quote-yellow);
    font-family: "Poiret One", "Questrial", sans-serif;
    font-weight: 400;
  }
  .quote span {
    position: absolute;
    line-height: 1;
    white-space: nowrap;
  }
  .quote__lead {
    left: 138px;
    top: 348px;
    font-size: 114px;
    letter-spacing: 1px;
  }
  .quote__bridge {
    left: 445px;
    top: 493px;
    font-size: 38px;
  }
  .quote__close {
    left: 44px;
    top: 530px;
    font-size: 130px;
    letter-spacing: 1px;
  }
  .source-ring {
    position: absolute;
    left: 289px;
    top: 745px;
    width: 270px;
    height: 270px;
  }
  .source {
    position: absolute;
    left: 368px;
    top: 866px;
    color: var(--source-white);
    font-family: "Questrial", sans-serif;
    font-size: 27px;
    line-height: 1;
    white-space: nowrap;
  }
  .source__given { margin-right: 10px; }
</style>
</head>
<body>
  <main class="poster">
    <blockquote class="quote">
      <span class="quote__lead">Simplicity</span>
      <span class="quote__bridge">is the ultimate in</span>
      <span class="quote__close">sophistication</span>
    </blockquote>

    <svg class="source-ring" viewBox="0 0 270 270" aria-hidden="true">
      <circle cx="135" cy="135" r="133" fill="none" stroke="var(--quote-yellow)" stroke-width="2.5"/>
    </svg>

    <cite class="source"><span class="source__given">Rinaldo</span>de Pavesco</cite>
  </main>
</body>
</html>
```